Website design for a construction company

The logo and the copies of all the 3 pages are attached below. I don't have a preference in colors but I would ideally like to use the colors on my logo, dark teal (secondary) and copper (primary).

Company Name: Talvarin Group

Location: London, UK

Business Overview:

Talvarin Group is a comprehensive construction company based in London, specializing in a wide range of construction services. We cater to various sectors, providing services including electrical work, painting and decorating, plastering, plumbing, carpentry, kitchen and bathroom installations, loft conversions, and extensions. Our team is known for its skilled craftsmanship, attention to detail, and commitment to quality.

What "TALVARIN" stands for:

Our company name, 'TALVARIN', is derived from Talvarion, the ancient Greek god of craftsmen, blacksmiths, artisans, sculptors, metals, metallurgy, fire, and volcanoes. Talvarion was renowned in mythology for his incredible skill in crafting and creating, making him the patron of all craftsmen and artisans. His name is synonymous with the mastery of artisanship and the creation of wondrous, enduring works.

In choosing 'TALVARIN' as our name, we embody the spirit and skills of Talvarion. It reflects our commitment to craftsmanship, excellence, and durability in the field of construction. Just as Talvarion was known for his meticulous work, precision, and innovative creations, our company strives to uphold these qualities in every project we undertake.

Our name is a constant reminder of our dedication to quality, innovation, and the art of building. It symbolizes our endeavor to achieve the highest standards in construction, much like Talvarion did in his timeless creations. In essence, 'TALVARIN' is not just our name; it's a representation of our ethos and the high standards we set for ourselves in the construction industry.

Target Audience:

Our primary audience includes homeowners, real estate developers, and commercial clients in London seeking reliable, high-quality construction services.

Unique Selling Points:

Diverse Range of Services: Offering a one-stop solution for all construction needs.

Certified and Experienced: Professional team with a strong focus on delivering certified and compliant work, particularly in electrical services.

Client-Centric Approach: Emphasizing client satisfaction, we tailor our services to meet the unique needs and visions of our clients.

Quality and Reliability: Commitment to high-quality materials, skilled workmanship, and delivering projects on time and within budget.

Website Requirements:

Clean, professional design reflecting the quality and reliability of our services.

User-friendly navigation to easily access information about our services, portfolio, company background, and contact details.

Portfolio section showcasing our past projects with placeholders for images and descriptions.

Integration of a contact form, map for our location, and links to our social media accounts.

Mobile-responsive design to ensure accessibility across various devices.

Purpose of the Website:
The website aims to:

Establish an online presence and credibility in the construction industry.

Provide an informative resource about our services and past projects to potential clients.

Facilitate easy communication and inquiries through an integrated contact system.

Tone and Style:

Professional, informative, and welcoming. The website should convey trustworthiness and expertise in the construction field.

Target Market(s)

homeowners, real estate developers, and commercial clients

Industry/Entity Type

Construction

Number of Pages Required

3 page

Colors

Designer to choose colors to be used in the design.

```html
<!DOCTYPE html>
<html lang="en">
<head>
<meta charset="utf-8">
<title>Talvarin Group — Construction in London</title>
<link rel="stylesheet" href="https://fonts.googleapis.com/css2?family=Poppins:wght@400;500;600;700&family=Roboto:wght@700;900&display=swap">
<style>
:root{
  --copper:#c2500f;
  --copper-deep:#a9420b;
  --footer:#b44a12;
  --ink:#222;
  --muted:#555;
  --dark:#2a160c;
  --light:#f4f4f4;
  --white:#fff;
  --black:#0d0d0d;
}
*{margin:0;padding:0;box-sizing:border-box}
html,body{width:1200px;height:4284px;overflow:hidden}
body{font-family:"Poppins",sans-serif;color:var(--ink);background:var(--white);position:relative}
.abs{position:absolute}
.section-title{position:absolute;left:0;width:1200px;text-align:center;font-family:"Roboto",sans-serif;font-weight:900;font-size:40px;color:var(--copper);letter-spacing:.5px}
.section-lead{position:absolute;left:300px;width:600px;text-align:center;font-size:15px;line-height:24px;color:var(--muted)}
.btn{display:inline-flex;align-items:center;justify-content:center;background:var(--copper);color:var(--white);font-size:15px;font-weight:500}

/* header */
.site-header{position:absolute;left:0;top:0;width:1200px;height:112px;background:var(--white)}
.brand{position:absolute;left:40px;top:34px;font-size:34px;font-weight:600;color:var(--copper)}
.nav{position:absolute;left:478px;top:44px;display:flex;gap:30px;font-size:16px;color:var(--ink)}
.nav .active{color:var(--copper);border-bottom:2px solid var(--copper);padding-bottom:4px}
.nav-cta{position:absolute;left:990px;top:34px;width:130px;height:42px}

/* hero */
.hero{position:absolute;left:0;top:112px;width:1200px;height:648px;background:linear-gradient(180deg,#3b3a44 0%,#7c4a2c 45%,#c46a2a 70%,#3a2418 100%)}
.hero-shade{position:absolute;inset:0;background:rgba(0,0,0,.28)}
.hero-title{position:absolute;left:0;top:92px;width:1200px;text-align:center;color:var(--white);font-family:"Roboto",sans-serif;font-weight:900;font-size:46px;letter-spacing:1px}
.hero-sub{position:absolute;left:0;top:160px;width:1200px;text-align:center;color:var(--white);font-size:22px;font-weight:500}
.hero-btn{position:absolute;left:528px;top:218px;width:144px;height:46px}

/* welcome */
.welcome-text{top:878px;left:230px;width:740px}

/* why */
.why{position:absolute;left:40px;top:992px;width:1120px;height:448px;background:linear-gradient(135deg,#3a1f10,#1e0f08 60%,#4a2814)}
.why-title{position:absolute;left:0;top:82px;width:1120px;text-align:center;font-family:"Roboto",sans-serif;font-weight:900;font-size:40px;color:var(--white)}
.why-card{position:absolute;top:176px;width:340px;height:232px;border:2px solid rgba(255,255,255,.85);background:rgba(0,0,0,.25);padding:26px 22px;text-align:center}
.why-card h3{color:#e46a1f;font-size:19px;font-weight:600;text-transform:uppercase;margin-bottom:14px}
.why-card p{color:var(--white);font-size:14px;line-height:23px}

/* services */
.service-label{position:absolute;font-size:16px;color:var(--copper);line-height:22px}
.service-label.left{text-align:right;width:220px}

/* portfolio */
.portfolio{position:absolute;left:0;top:2280px;width:1200px;height:920px;background:var(--light)}
.project-feature{position:absolute;left:72px;top:216px;width:696px;height:300px;background:linear-gradient(120deg,#5a2a10,#8a4418 60%,#3a1c0c)}
.project-feature-overlay{position:absolute;left:0;top:0;width:696px;height:300px;background:rgba(90,35,8,.55);padding:34px 36px;color:var(--white)}
.project-feature h3{font-size:22px;font-weight:600;line-height:30px;text-transform:uppercase;width:520px}
.project-feature p{font-size:14px;line-height:21px;margin-top:14px;width:560px}
.outline-btn{display:inline-flex;margin-top:18px;width:130px;height:42px;border:1px solid var(--white);align-items:center;justify-content:center;font-size:14px}
.project-photo{position:absolute}

/* testimonials */
.avatar{position:absolute;border-radius:50%}
.client-name{position:absolute;left:0;top:3494px;width:1200px;text-align:center;font-size:22px;font-weight:600}
.client-role{position:absolute;left:0;top:3528px;width:1200px;text-align:center;font-size:17px;color:var(--copper)}
.client-quote{position:absolute;left:320px;top:3594px;width:560px;text-align:center;font-size:15px;line-height:22px;color:var(--muted)}

/* footer */
.site-footer{position:absolute;left:0;top:3780px;width:1200px;height:400px;background:var(--footer);color:var(--white)}
.footer-col{position:absolute;top:88px}
.footer-col h4{font-size:21px;font-weight:500;margin-bottom:22px}
.footer-col h4 b{font-weight:700}
.footer-col li{list-style:none;font-size:15px;line-height:34px;display:flex;align-items:center;gap:14px}
.contact-row{display:flex;gap:18px;align-items:flex-start;font-size:14px;line-height:20px;margin-bottom:18px}
.bottom-bar{position:absolute;left:0;top:4180px;width:1200px;height:104px;background:var(--black);color:var(--white)}
.social{position:absolute;top:34px;width:36px;height:36px;border:2px solid var(--white);border-radius:50%}
.copyright{position:absolute;right:100px;top:40px;font-size:15px}
</style>
</head>
<body>

<header class="site-header">
  <div class="brand">Talvarin Group</div>
  <nav class="nav">
    <span class="active">Home</span><span>About Us</span><span>Our Services</span><span>Portfolio</span><span>Testimonials</span>
  </nav>
  <span class="btn nav-cta">Contact Us</span>
</header>

<section class="hero" role="img" aria-label="London city skyline at sunset">
  <div class="hero-shade"></div>
  <h1 class="hero-title">BUILDING YOUR DREAMS INTO REALITY</h1>
  <p class="hero-sub">Expert Craftsmanship Meets Unmatched Reliability in the Heart of London</p>
  <span class="btn hero-btn">Read More</span>
</section>

<h2 class="section-title" style="top:812px">WELCOME TO TALVARIN GROUP</h2>
<p class="section-lead welcome-text">Where Construction Meets Excellence. Based in London, we are committed to transforming your spaces into exceptional places. Our team is dedicated to delivering the highest quality in every project, attending to every detail with precision and care.</p>

<section class="why" role="img" aria-label="Dark construction site backdrop">
  <h2 class="why-title">WHY CHOOSE US</h2>
  <div class="why-card" style="left:18px">
    <h3>Our Expertise</h3>
    <p>"Leveraging over 10 years of experience, Talvarin Group stands as a beacon of excellence in the construction industry. We handle each project, big or small, with unmatched professionalism and skill."</p>
  </div>
  <div class="why-card" style="left:390px">
    <h3>Quality Assurance</h3>
    <p>"Quality is not just a promise, but a practice. Meticulous attention to detail ensures flawless finishes and durable structures, bringing long-lasting satisfaction to our clients."</p>
  </div>
  <div class="why-card" style="left:762px">
    <h3>Certified Excellence</h3>
    <p>"Your safety and satisfaction are our top priorities. We provide electrical certificates and adhere to the highest industry standards, offering peace of mind in every service."</p>
  </div>
</section>

<h2 class="section-title" style="top:1528px">OUR SERVICES</h2>
<p class="section-lead" style="top:1592px">Tailored to Your Needs. Discover how we can bring your vision to life, covering every aspect of construction from the initial design to the final touches.</p>

<svg class="abs" style="left:0;top:1680px" width="1200" height="540" viewBox="0 1680 1200 540">
  <defs>
    <linearGradient id="svcFill" x1="0" y1="0" x2="0" y2="1">
      <stop offset="0" stop-color="#c45a1e"/><stop offset="1" stop-color="#3a1c0c"/>
    </linearGradient>
    <g id="svcIcon">
      <circle r="26" fill="#c2500f"/>
      <path d="M-12 2 L0 -10 L12 2 M-8 -1 V11 H8 V-1" fill="none" stroke="#fff" stroke-width="2.4" stroke-linejoin="round"/>
    </g>
  </defs>
  <circle cx="600" cy="1940" r="180" fill="none" stroke="#e9b79a" stroke-width="2"/>
  <circle cx="600" cy="1940" r="136" fill="url(#svcFill)" role="img" aria-label="Renovated interior photo"/>
  <use href="#svcIcon" x="600" y="1732"/>
  <use href="#svcIcon" x="448" y="1820"/>
  <use href="#svcIcon" x="752" y="1820"/>
  <use href="#svcIcon" x="430" y="1940"/>
  <use href="#svcIcon" x="770" y="1940"/>
  <use href="#svcIcon" x="448" y="2060"/>
  <use href="#svcIcon" x="752" y="2060"/>
  <use href="#svcIcon" x="600" y="2148"/>
</svg>
<span class="service-label" style="left:556px;top:1672px;width:88px;text-align:center">Extensions</span>
<span class="service-label left" style="left:192px;top:1809px">Loft Conversions</span>
<span class="service-label" style="left:792px;top:1809px">Electrical Work</span>
<span class="service-label left" style="left:174px;top:1918px">Kitchen &amp; Bathroom<br>Installations</span>
<span class="service-label" style="left:810px;top:1929px">Painting and Decorating</span>
<span class="service-label left" style="left:192px;top:2049px">Carpentry</span>
<span class="service-label" style="left:792px;top:2049px">Plastering</span>
<span class="service-label" style="left:550px;top:2184px;width:100px;text-align:center">Plumbing</span>

<section class="portfolio">
  <h2 class="section-title" style="top:66px">OUR PORTFOLIO</h2>
  <p class="section-lead" style="top:128px">Tailored to Your Needs. Discover how we can bring your vision to life, covering every aspect of construction from the initial design to the final touches.</p>
  <div class="project-feature" role="img" aria-label="Interior of a finished project">
    <div class="project-feature-overlay">
      <h3>Lorem ipsum dolor sit amet, consectetur a lacus velfacilisis.</h3>
      <p>Lorem ipsum dolor sit amet, consectetur adipiscing elit, sed do eiusmod tempor incididunt ut labore et dolore magna aliqua. Quis ipsum suspendisse maecenas accumsan lacus vel facilisis.</p>
      <span class="outline-btn">Read More</span>
    </div>
  </div>
  <div class="project-photo" role="img" aria-label="City towers under construction with cranes" style="left:780px;top:216px;width:348px;height:640px;background:linear-gradient(180deg,#b9a89a 0%,#8c7d72 50%,#4d4038 100%)"></div>
  <div class="project-photo" role="img" aria-label="Building site with tower crane against blue sky" style="left:72px;top:524px;width:344px;height:332px;background:linear-gradient(180deg,#7aa7d4 0%,#a8bfd4 55%,#5a5a5a 100%)"></div>
  <div class="project-photo" role="img" aria-label="Modern white apartment building" style="left:424px;top:524px;width:344px;height:332px;background:linear-gradient(160deg,#3f6fb8 0%,#9db6d8 50%,#e8edf2 100%)"></div>
</section>

<h2 class="section-title" style="top:3250px">WHAT OUR CLIENT SAYS</h2>
<div class="avatar" role="img" aria-label="Client portrait" style="left:268px;top:3368px;width:72px;height:72px;background:#8a8a8a"></div>
<div class="avatar" role="img" aria-label="Client portrait" style="left:408px;top:3368px;width:72px;height:72px;background:#7a6a5c"></div>
<div class="avatar" role="img" aria-label="Client portrait" style="left:544px;top:3350px;width:112px;height:112px;background:#4f4a46;border:3px solid var(--white);box-shadow:0 0 0 1px #ddd"></div>
<div class="avatar" role="img" aria-label="Client portrait" style="left:720px;top:3368px;width:72px;height:72px;background:#6d6258"></div>
<div class="avatar" role="img" aria-label="Client portrait" style="left:852px;top:3368px;width:72px;height:72px;background:#a39485"></div>
<div class="client-name">Daniel</div>
<div class="client-role">Asst Manager</div>
<svg class="abs" style="left:540px;top:3560px" width="120" height="24" viewBox="0 0 120 24">
  <g fill="#e0a21a">
    <path id="star" d="M12 2l2.9 6.3 6.9.7-5.2 4.6 1.5 6.8L12 17l-6.1 3.4 1.5-6.8L2.2 9l6.9-.7z"/>
    <use href="#star" x="24"/><use href="#star" x="48"/><use href="#star" x="72"/><use href="#star" x="96"/>
  </g>
</svg>
<p class="client-quote">Lorem ipsum dolor sit amet, consectetur adipiscing elit, sed do eiusmod tempor incididunt ut labore et dolore magna aliqua. Quis ipsum suspendisse ultrices gravida. Risus commodo viverra maecenas accumsan lacus vel facilisis.</p>
<svg class="abs" style="left:130px;top:3510px" width="44" height="44" viewBox="0 0 44 44"><circle cx="22" cy="22" r="22" fill="#c2500f"/><path d="M25 14l-8 8 8 8" fill="none" stroke="#fff" stroke-width="3"/></svg>
<svg class="abs" style="left:1026px;top:3510px" width="44" height="44" viewBox="0 0 44 44"><circle cx="22" cy="22" r="22" fill="#c2500f"/><path d="M19 14l8 8-8 8" fill="none" stroke="#fff" stroke-width="3"/></svg>
<svg class="abs" style="left:576px;top:3712px" width="48" height="12" viewBox="0 0 48 12">
  <circle cx="6" cy="6" r="5" fill="#c2500f"/><circle cx="24" cy="6" r="5" fill="#c2500f" opacity=".45"/><circle cx="42" cy="6" r="5" fill="#c2500f" opacity=".45"/>
</svg>

<footer class="site-footer">
  <div class="footer-col" style="left:208px">
    <h4><b>Quick</b> Links</h4>
    <ul>
      <li>›&nbsp;Home</li><li>›&nbsp;About Us</li><li>›&nbsp;Our Services</li><li>›&nbsp;Our Blogs</li><li>›&nbsp;Testimonials</li>
    </ul>
  </div>
  <div class="footer-col" style="left:488px">
    <h4><b>Customer</b> Services</h4>
    <ul>
      <li>›&nbsp;Contact us</li><li>›&nbsp;Site Map</li><li>›&nbsp;Terms and Use</li><li>›&nbsp;My Account</li>
    </ul>
  </div>
  <div class="footer-col" style="left:756px">
    <h4><b>Our</b> Newsletter</h4>
    <div class="contact-row" style="margin-top:36px">
      <svg width="24" height="24" viewBox="0 0 24 24"><rect x="1" y="1" width="22" height="22" rx="3" fill="none" stroke="#fff" stroke-width="1.6"/><path d="M8 6l2 3-1.5 1.5a7 7 0 0 0 5 5L15 14l3 2-1 2c-5 0-11-6-11-11z" fill="#fff"/></svg>
      <span>CALL US<br>(020) 555-0148</span>
    </div>
    <div class="contact-row">
      <svg width="24" height="24" viewBox="0 0 24 24"><rect x="1" y="1" width="22" height="22" rx="3" fill="none" stroke="#fff" stroke-width="1.6"/><rect x="5" y="7" width="14" height="10" fill="none" stroke="#fff" stroke-width="1.6"/><path d="M5 7l7 6 7-6" fill="none" stroke="#fff" stroke-width="1.6"/></svg>
      <span>EMAIL US<br>info@talvaringroup.example</span>
    </div>
    <div class="contact-row">
      <svg width="24" height="24" viewBox="0 0 24 24"><rect x="1" y="1" width="22" height="22" rx="3" fill="none" stroke="#fff" stroke-width="1.6"/><path d="M12 19s-5-5-5-9a5 5 0 0 1 10 0c0 4-5 9-5 9z" fill="#fff"/><circle cx="12" cy="10" r="2" fill="#b44a12"/></svg>
      <span>118 Harbour Lane, Suite 4<br>Millbrook, London E14 5QT</span>
    </div>
  </div>
</footer>

<div class="bottom-bar">
  <span class="social" style="left:100px"></span>
  <span class="social" style="left:146px"></span>
  <span class="social" style="left:192px"></span>
  <span class="social" style="left:238px"></span>
  <span class="copyright">All Rights Reserved @ Copyrights 2023</span>
</div>

</body>
</html>
```